Bref créative
Stationery for an intellectual property right service provider
ZENOLT
Simple
Tarek Baduri
CEO
Lövbergsvägen 7
164 52 Kallbacka
Nordrika
tarek.baduri@zenolt.eu
www.zenolt.eu

```html
<!DOCTYPE html>
<html lang="en">
<head>
<meta charset="utf-8">
<title>ZENOLT – Business Card</title>
<link href="https://fonts.googleapis.com/css2?family=Tinos:wght@400;700&display=swap" rel="stylesheet">
<style>
  :root {
    --bg: #e9e9ea;
    --red: #d5101c;
    --red-dark: #a8070f;
    --red-light: #ea2a33;
    --grey: #8a8a8c;
    --grey-light: #c9c9cb;
    --ink: #3a3a3c;
    --white: #ffffff;
  }
  * { box-sizing: border-box; margin: 0; padding: 0; }
  html, body {
    width: 1200px; height: 1009px; overflow: hidden;
    background: var(--bg);
    font-family: "Tinos", "Times New Roman", serif;
  }
  .card {
    position: absolute; left: 170px;
    width: 860px; height: 470px;
    border-radius: 26px; overflow: hidden;
    box-shadow: 0 6px 18px rgba(0,0,0,.18);
  }
  .card--back { top: 22px; background: linear-gradient(160deg, var(--red-light) 0%, var(--red) 45%, var(--red-dark) 100%); }
  .card--front { top: 516px; background: var(--white); }

  .card__art { position: absolute; inset: 0; width: 100%; height: 100%; }

  .brand { position: absolute; display: flex; align-items: center; }
  .brand__name { font-weight: 400; letter-spacing: 2px; line-height: 1; white-space: nowrap; }
  .brand__rule { width: 1px; align-self: stretch; margin: 0 16px; }
  .brand__tagline { text-transform: uppercase; letter-spacing: 1.5px; line-height: 1.35; white-space: nowrap; }

  .card--back .brand { left: 250px; top: 190px; }
  .card--back .brand__name { color: var(--white); font-size: 70px; }
  .card--back .brand__rule { background: var(--white); }
  .card--back .brand__tagline { color: var(--white); font-size: 14px; }

  .card--front .brand { left: 48px; top: 44px; }
  .card--front .brand__name { color: var(--red); font-size: 46px; }
  .card--front .brand__rule { background: var(--grey); margin: 0 12px; }
  .card--front .brand__tagline { color: var(--grey); font-size: 10px; }

  .contact { position: absolute; left: 50px; top: 130px; list-style: none; color: var(--ink); font-size: 17px; }
  .contact__item { display: flex; align-items: center; height: 28px; white-space: nowrap; }
  .contact__icon { width: 14px; height: 14px; margin-right: 10px; flex: none; }
  .contact__item--plain { padding-left: 24px; }

  .person { position: absolute; right: 52px; bottom: 40px; text-align: right; }
  .person__name { color: var(--red); font-size: 30px; }
  .person__role { color: var(--grey); font-size: 20px; margin-top: 6px; }
</style>
</head>
<body>

<section class="card card--back">
  <div class="brand">
    <span class="brand__name">ZENOLT</span>
    <span class="brand__rule"></span>
    <span class="brand__tagline">Intellectual<br>Property Rights<br>and Innovation Services</span>
  </div>
</section>

<section class="card card--front">
  <svg class="card__art" viewBox="0 0 860 470" preserveAspectRatio="none" aria-hidden="true">
    <defs>
      <linearGradient id="redFill" x1="0" y1="0" x2="1" y2="1">
        <stop offset="0" stop-color="#ea2a33"/>
        <stop offset="1" stop-color="#b0080f"/>
      </linearGradient>
      <linearGradient id="greyBand" x1="0" y1="0" x2="1" y2="0">
        <stop offset="0" stop-color="#e4e4e5"/>
        <stop offset="1" stop-color="#9c9c9e"/>
      </linearGradient>
    </defs>
    <path d="M440,0 H480 C525,150 515,320 445,470 H405 C480,320 490,150 440,0 Z" fill="url(#greyBand)"/>
    <path d="M480,0 H860 V290 C700,300 565,370 505,470 H445 C515,320 525,150 480,0 Z" fill="url(#redFill)"/>
  </svg>

  <div class="brand">
    <span class="brand__name">ZENOLT</span>
    <span class="brand__rule"></span>
    <span class="brand__tagline">Intellectual<br>Property Rights<br>and Innovation Services</span>
  </div>

  <ul class="contact">
    <li class="contact__item contact__item--plain">Lövbergsvägen 7</li>
    <li class="contact__item contact__item--plain">164 52 Kallbacka, Nordrika</li>
    <li class="contact__item">
      <svg class="contact__icon" viewBox="0 0 14 14"><path d="M3 1 L5.5 1 L6.5 4 L5 5.2 C5.8 7 7 8.2 8.8 9 L10 7.5 L13 8.5 L13 11 C13 12 12 13 11 13 C5.5 12.6 1.4 8.5 1 3 C1 2 2 1 3 1 Z" fill="var(--red)"/></svg>
      +46 (0)8 55 21 90
    </li>
    <li class="contact__item">
      <svg class="contact__icon" viewBox="0 0 14 14"><rect x="3.5" y="0.5" width="7" height="13" rx="1.5" fill="var(--red)"/><rect x="5" y="2.5" width="4" height="7" fill="#fff"/></svg>
      +46 (0)70 38 16 42
    </li>
    <li class="contact__item">
      <svg class="contact__icon" viewBox="0 0 14 14"><rect x="0.5" y="2.5" width="13" height="9" fill="var(--red)"/><path d="M1 3 L7 8 L13 3" stroke="#fff" stroke-width="1.2" fill="none"/></svg>
      tarek.baduri@zenolt.eu
    </li>
    <li class="contact__item">
      <svg class="contact__icon" viewBox="0 0 14 14"><circle cx="7" cy="7" r="6.3" fill="var(--red)"/><path d="M1 7 H13 M7 1 C4 4 4 10 7 13 M7 1 C10 4 10 10 7 13" stroke="#fff" stroke-width="1" fill="none"/></svg>
      www.zenolt.eu
    </li>
  </ul>

  <div class="person">
    <div class="person__name">Tarek Baduri</div>
    <div class="person__role">CEO</div>
  </div>
</section>

</body>
</html>
```